Willowmere Spa and Beauty Ltd. (Name of business)

I need a business card designed for this new company based out of Toronto Ontario. We specialize in Eyelash Extensions, Manicures and Pedicures, body waxing, massages, laser hair removal and botox treatments. Also offer a variety of products for sale, such as skin cream serums, collagen gel, eye cream, etc. It is a safe relaxing and non-judgemental environnment. Clients are welcome to come be pampered for the half or full day. Many service packages to choose from.

Open 7days per week from 8am to 8pm.

Marissa Thornbury
Spa Facilitator
Willowmere Spa and Beauty Ltd.
7200 Calder Ave; Suite 1400
Toronto ON K8P 2W7

OFFICE: 416.739.4100
FAX: 416.739.4101
CELL: 416.582.6074
EMAIL: marissa.thornbury@willowmerespa.example

Target Market(s)

Target market is primarily female ranging from 16 years old to 50 years old.

Industry/Entity Type

Business

Contact Information for Business Card

Marissa Thornbury
Spa Facilitator
7200 Calder Ave; Suite 1400
Toronto ON K8P 2W7

OFFICE: 416.739.4100
FAX: 416.739.4101
CELL: 416.582.6074

Logo Text

I dont have a logo yet. I would like it simple but sophisticated and modern.

Font styles to use
Serif

Requirements
Must have
• all pertinent details such as company name, logo, name and contact information, services that are offered, including package rates
Nice to have
• Company name and logo prominent. A card that is neat and the information such as address, phone number, fax, email, etc is not too crowded but laid out in an easy to read format.
• Possibly on the back of card - some of the services offered could be listed, as well as professional cream lotions and serums. Hours of operation etc.

```html
<!DOCTYPE html>
<html lang="en">
<head>
<meta charset="utf-8">
<title>Willowmere Spa and Beauty Ltd. – Business Card</title>
<link href="https://fonts.googleapis.com/css2?family=Lora:ital,wght@0,400;0,500;1,400&display=swap" rel="stylesheet">
<style>
  :root {
    --stage: #2d2d2d;
    --card-white: #ffffff;
    --mauve: #9a6679;
    --mauve-deep: #8a5a6c;
    --pink: #e0609e;
    --brand-pink: #c0528a;
    --ink: #555555;
    --ink-soft: #666666;
    --rule: #8a8a8a;
    --on-dark: #ffffff;
  }
  * { box-sizing: border-box; margin: 0; padding: 0; }
  html, body { width: 1200px; height: 900px; overflow: hidden; }
  body {
    background: var(--stage);
    font-family: "Lora", Georgia, serif;
    position: relative;
  }
  .card {
    position: absolute;
    left: 270px;
    width: 652px;
    height: 381px;
    border-radius: 22px;
    overflow: hidden;
  }

  /* Front */
  .card-front { top: 49px; background: var(--card-white); }
  .front-waves { position: absolute; inset: 0; width: 652px; height: 381px; }
  .brand-front {
    position: absolute;
    left: 40px; top: 150px; width: 270px;
    text-align: center;
    color: var(--brand-pink);
    font-weight: 400;
    line-height: 1.25;
  }
  .brand-front .brand-name { font-size: 30px; display: block; }
  .brand-front .brand-sub { font-size: 18px; display: block; }
  .divider {
    position: absolute; left: 322px; top: 56px;
    width: 1px; height: 183px; background: var(--rule);
  }
  .contact { position: absolute; left: 342px; top: 58px; width: 296px; color: var(--ink); }
  .contact .person { font-size: 20px; font-weight: 500; line-height: 1.2; }
  .contact .role { font-size: 14.5px; font-style: italic; color: var(--pink); margin-top: 1px; }
  .contact .address { font-size: 15px; line-height: 18px; margin-top: 10px; color: var(--ink-soft); }
  .contact .lines { list-style: none; margin-top: 13px; font-size: 15px; line-height: 18.5px; color: var(--ink-soft); }
  .contact .lines li { display: flex; align-items: center; gap: 8px; white-space: nowrap; }
  .contact .lines li.email { font-size: 13.5px; letter-spacing: -0.1px; }
  .contact .lines svg { width: 12px; height: 12px; fill: var(--ink); flex: none; }
  .hours {
    position: absolute; left: 0; right: 0; top: 341px;
    text-align: center; color: var(--on-dark);
    font-size: 17px; font-weight: 500;
  }

  /* Back */
  .card-back {
    top: 465px;
    background:
      radial-gradient(circle at 100% 12%, var(--pink) 0%, rgba(224,96,158,0.55) 22%, rgba(154,102,121,0) 48%),
      var(--mauve);
  }
  .decor-area {
    position: absolute; left: 0; top: 0; width: 230px; height: 381px;
    background: linear-gradient(90deg, rgba(255,255,255,0.12), rgba(255,255,255,0.05) 55%, rgba(255,255,255,0) 100%);
  }
  .brand-back {
    position: absolute; left: 0; right: 0; top: 150px;
    text-align: center; color: var(--on-dark); font-weight: 400; line-height: 1.25;
  }
  .brand-back .brand-name { font-size: 32px; display: block; }
  .brand-back .brand-sub { font-size: 18px; display: block; }
  .rule {
    position: absolute; left: 110px; width: 435px; height: 1px;
    background: linear-gradient(90deg, rgba(255,255,255,0), rgba(255,255,255,0.9) 50%, rgba(255,255,255,0));
  }
  .rule-top { top: 233px; }
  .rule-mid { top: 305px; }
  .offer {
    position: absolute; left: 0; right: 0;
    text-align: center; color: var(--on-dark);
  }
  .offer h2 { font-size: 17px; font-weight: 500; line-height: 20px; }
  .offer p { font-size: 14.5px; line-height: 18px; }
  .offer-services { top: 239px; }
  .offer-products { top: 314px; }
</style>
</head>
<body>

<section class="card card-front" aria-label="Business card front">
  <svg class="front-waves" viewBox="0 0 652 381" aria-hidden="true">
    <path d="M0,318 C140,300 300,294 400,304 C480,312 560,318 652,290 L652,381 L0,381 Z" fill="#9a6679"/>
    <path d="M0,344 C120,320 250,309 410,308 C250,318 120,336 0,366 Z" fill="#ffffff"/>
    <path d="M370,318 C500,332 600,318 652,258 L652,284 C600,334 490,338 370,318 Z" fill="#e0609e"/>
  </svg>

  <div class="brand-front">
    <span class="brand-name">Willowmere Spa</span>
    <span class="brand-sub">and Beauty Ltd.</span>
  </div>

  <div class="divider"></div>

  <div class="contact">
    <div class="person">Marissa Thornbury</div>
    <div class="role">Spa Facilitator</div>
    <div class="address">7200 Calder Ave; Suite 1400<br>Toronto ON K8P 2W7</div>
    <ul class="lines">
      <li><svg viewBox="0 0 12 12"><path d="M2.5 0.8l2 2.2-1.1 1.4c.7 1.5 1.8 2.6 3.3 3.3l1.4-1.1 2.2 2-1.3 1.9C4.8 10.3 1.7 7.2 0.6 2.1z"/></svg>416.739.4100</li>
      <li><svg viewBox="0 0 12 12"><path d="M3 1h6v3H3z M1 4.5h10v5H9V8H3v1.5H1z M3 8.5h6V11H3z"/></svg>416.739.4101</li>
      <li><svg viewBox="0 0 12 12"><path d="M3 0.5h6v11H3z M4 1.8v7.4h4V1.8z" fill-rule="evenodd"/></svg>416.582.6074</li>
      <li class="email"><svg viewBox="0 0 12 12"><path d="M1 2.5h10L6 6.5z M1 3.8l5 4 5-4V9.5H1z"/></svg>marissa.thornbury@willowmerespa.example</li>
    </ul>
  </div>

  <div class="hours">Open 7days per week from 8am to 8pm.</div>
</section>

<section class="card card-back" aria-label="Business card back">
  <div class="decor-area" role="img" aria-label="Faint decorative silhouette artwork in soft mauve tones"></div>

  <div class="brand-back">
    <span class="brand-name">Willowmere Spa</span>
    <span class="brand-sub">and Beauty Ltd.</span>
  </div>

  <div class="rule rule-top"></div>
  <div class="offer offer-services">
    <h2>Services</h2>
    <p>Eyelash Extensions | Manicures and Pedicures | body waxing massages</p>
    <p>laser hair removal | botox treatments</p>
  </div>

  <div class="rule rule-mid"></div>
  <div class="offer offer-products">
    <h2>Products for sale</h2>
    <p>skin cream serums &nbsp;|&nbsp; collagen gel &nbsp;|&nbsp; eye cream, etc.</p>
  </div>
</section>

</body>
</html>
```